4747 5858

Web(re)design of an existing directory search site www.le5858.be (in Dutch www.de4747.be and in English www.3737.be).

This site is a directory site, i.e. a "white pages" site whereby people can search the phone & details of another person based on a combination of name + city (for instance pellow in Brussels); one can also search a company also based on a combination of name + city (for instance Vornak in Brussels); last but not least one can also search the name of the subscriber behind a specific telephone number (also called reverse search).

This site is quite outdated and needs a redesign, see instructions.

We need the output in XD format.

```html
<!DOCTYPE html>
<html lang="fr">
<head>
<meta charset="utf-8">
<title>Annuo — Annuaire</title>
<link rel="stylesheet" href="https://fonts.googleapis.com/css2?family=Noto+Sans:wght@400;500;700;900&display=swap">
<style>
  :root {
    --navy: #072a5c;
    --navy-text: #163d6f;
    --grey-text: #4a5566;
    --border: #9aa3ad;
    --card-border: #c9ced4;
    --white: #ffffff;
    --forest-dark: #2c3520;
    --forest-mid: #5a6a3a;
    --forest-light: #8d8a5a;
  }
  * { box-sizing: border-box; margin: 0; padding: 0; }
  html, body { width: 1200px; height: 796px; overflow: hidden; background: var(--white); }
  body { font-family: "Noto Sans", sans-serif; color: var(--navy-text); position: relative; }

  .brand {
    position: absolute; left: 68px; top: 42px;
    display: flex; align-items: center; gap: 10px;
    font-size: 26px; font-weight: 500; color: var(--navy-text);
  }
  .brand-mark { width: 18px; height: 18px; background: var(--navy-text); }

  .top-nav { position: absolute; top: 50px; left: 710px; display: flex; align-items: center; font-size: 15px; }
  .top-nav a { color: var(--navy-text); text-decoration: none; display: flex; align-items: center; gap: 9px; }
  .nav-home { margin-right: 64px; }
  .nav-help { margin-right: 64px; }
  .lang { display: flex; align-items: center; gap: 12px; color: var(--grey-text); }
  .flag { display: flex; width: 34px; height: 23px; }
  .flag span { flex: 1; }
  .flag .blue { background: #0a2a63; }
  .flag .white { background: var(--white); }
  .flag .red { background: #e3172b; }

  .tabs { position: absolute; top: 130px; left: 159px; display: flex; gap: 58px; font-size: 22.5px; font-weight: 500; }
  .tab { color: var(--navy-text); position: relative; padding-bottom: 8px; }
  .tab.active::after { content: ""; position: absolute; left: -2px; right: -7px; bottom: -2px; height: 2px; background: var(--navy-text); }

  .hero {
    position: absolute; left: 67px; top: 190px; width: 1066px; height: 435px;
    border-radius: 19px; overflow: hidden;
    background:
      radial-gradient(ellipse at 78% 55%, rgba(200,196,160,.55), transparent 35%),
      radial-gradient(ellipse at 55% 70%, rgba(190,175,130,.5), transparent 30%),
      radial-gradient(ellipse at 30% 85%, rgba(80,120,50,.6), transparent 40%),
      linear-gradient(110deg, var(--forest-dark), var(--forest-mid) 45%, var(--forest-light) 70%, var(--forest-dark));
  }
  .hero-title { position: absolute; left: 53px; top: 102px; color: var(--white); text-shadow: 0 2px 6px rgba(0,0,0,.35); }
  .hero-title .lead { display: block; font-size: 54px; font-weight: 400; letter-spacing: .5px; line-height: 1; }
  .hero-title .strong { display: block; font-size: 76px; font-weight: 900; line-height: 1; margin-top: 10px; letter-spacing: 1px; }

  .search-card {
    position: absolute; left: 106px; top: 577px; width: 989px; height: 135px;
    background: var(--white); border: 1px solid var(--card-border); border-radius: 10px;
    box-shadow: 0 4px 12px rgba(0,0,0,.08);
  }
  .field { position: absolute; top: 26px; width: 233px; }
  .field label { display: flex; align-items: center; gap: 10px; font-size: 21px; font-weight: 500; color: var(--navy-text); height: 28px; }
  .field input {
    margin-top: 8px; width: 233px; height: 49px; border: 1px solid var(--border);
    padding: 0 9px; font: 400 15px "Noto Sans", sans-serif; color: var(--grey-text);
  }
  .field input::placeholder { color: #2c3440; }
  .field-surname { left: 29px; }
  .field-first { left: 296px; }
  .field-locality { left: 568px; }
  .search-btn {
    position: absolute; left: 835px; top: 62px; width: 122px; height: 49px;
    background: var(--navy); color: var(--white); border: none; border-radius: 3px;
    font: 400 22px "Noto Sans", sans-serif;
  }
</style>
</head>
<body>
  <div class="brand"><span class="brand-mark"></span>Annuo</div>

  <nav class="top-nav">
    <a class="nav-home" href="#">
      <svg width="17" height="17" viewBox="0 0 24 24" fill="none" stroke="#8a93a8" stroke-width="2"><path d="M3 11 12 3l9 8"/><path d="M5 10v11h5v-6h4v6h5V10"/></svg>
      Home</a>
    <a class="nav-help" href="#">
      <svg width="17" height="17" viewBox="0 0 24 24" fill="none" stroke="#8a93a8" stroke-width="2"><circle cx="12" cy="12" r="9"/><circle cx="12" cy="12" r="4"/><path d="M5.6 5.6l3.6 3.6M18.4 5.6l-3.6 3.6M5.6 18.4l3.6-3.6M18.4 18.4l-3.6-3.6"/></svg>
      Help Center</a>
    <div class="lang">
      <div class="flag"><span class="blue"></span><span class="white"></span><span class="red"></span></div>
      Francais
      <svg width="12" height="12" viewBox="0 0 12 12" fill="none" stroke="#8a93a8" stroke-width="1.5"><path d="M1 4l5 5 5-5"/></svg>
    </div>
  </nav>

  <nav class="tabs">
    <span class="tab active">Particuliers</span>
    <span class="tab">Societes</span>
    <span class="tab">Annuaire Inverse</span>
    <span class="tab">International</span>
  </nav>

  <section class="hero" role="img" aria-label="Photo: a young man with a backpack sitting beside a large white dog in a pine forest">
    <h1 class="hero-title">
      <span class="lead">Lesrenseignemints</span>
      <span class="strong">VRAIMENT utiles</span>
    </h1>
  </section>

  <form class="search-card">
    <div class="field field-surname">
      <label><svg width="20" height="22" viewBox="0 0 20 22" fill="var(--navy)"><circle cx="10" cy="5.5" r="5"/><path d="M0 22c0-7 4-10 10-10s10 3 10 10z"/></svg>Surname</label>
      <input type="text" placeholder="Ex: Dupont, Janssens, ...">
    </div>
    <div class="field field-first">
      <label><svg width="22" height="22" viewBox="0 0 22 22"><circle cx="11" cy="11" r="11" fill="var(--navy)"/><circle cx="11" cy="8.5" r="3.6" fill="#fff"/><path d="M4.5 18c1.5-3.5 3.8-4.5 6.5-4.5s5 1 6.5 4.5" fill="#fff"/></svg>First Name</label>
      <input type="text" placeholder="Ex: Jan, Louis, ...">
    </div>
    <div class="field field-locality">
      <label><svg width="18" height="23" viewBox="0 0 18 23"><path d="M9 0C4 0 0 4 0 9c0 6 9 14 9 14s9-8 9-14c0-5-4-9-9-9z" fill="var(--navy)"/><circle cx="9" cy="9" r="3.5" fill="#fff"/></svg>Locality</label>
      <input type="text" placeholder="Ex: Liege, Antwerp, 1150 ...">
    </div>
    <button class="search-btn" type="button">Annuo!</button>
  </form>
</body>
</html>
```